Powerpoint template for company specialized in training and coaching

We are a company specialized in training and transforming Leaders of companies in their leadership skills. We also help companies transform their company culture. We look at what is positive and already works for the company. We need a powerpoint template for out training. The look and feel should be professional, warm and personal. We just launched our new website www.bridgeofvalor.nl so you can get a good feel. please also check our social media posts. Usually the diagonal stripes of our logo (the house) comes back here. https://www.linkedin.com/school/18294056/admin/feed/posts/
We need two template. One in our business colors https://bridgeofvalor.nl/zakelijk/ and one in our educational colors. https://bridgeofvalor.nl/opleidingen/.

```html
<!DOCTYPE html>
<html lang="en">
<head>
<meta charset="utf-8">
<title>Bridge of Valor – Presentation Template</title>
<link rel="stylesheet" href="https://fonts.googleapis.com/css2?family=Montserrat:wght@600;700;800&family=Roboto:wght@400;500;700&display=swap">
<style>
  :root{
    --canvas:#dcdcdc;
    --ink:#1d2426;
    --copy:#555b5d;
    --quote-name:#2f4a6a;
    --business:#3f6269;
    --business-tint:#eef8fa;
    --education:#b06232;
    --education-tint:#fdf3ee;
  }
  *{box-sizing:border-box;margin:0;padding:0}
  html,body{width:772px;height:1200px;overflow:hidden}
  body{background:var(--canvas);position:relative;font-family:Roboto,sans-serif}

  .theme-business{--accent:var(--business);--tint:var(--business-tint)}
  .theme-education{--accent:var(--education);--tint:var(--education-tint)}

  .slide{position:absolute;width:311px;height:175px;background:#fff;overflow:hidden;box-shadow:0 1px 3px rgba(0,0,0,.12)}
  .col-left{left:51.5px}
  .col-right{left:409.5px}
  .row-1{top:28px}.row-2{top:222px}.row-3{top:415.5px}
  .row-4{top:609.5px}.row-5{top:803px}.row-6{top:997px}

  /* cover */
  .cover{background:var(--accent)}
  .cover-photo{position:absolute;inset:0;background:radial-gradient(ellipse at 70% 40%,rgba(255,255,255,.10),rgba(0,0,0,.08) 70%)}
  .cover-brand{position:absolute;top:25px;left:0;width:100%;display:flex;justify-content:center;align-items:center;gap:4px}
  .cover-brand .brand-mark{width:15px;height:15px;background:#fff}
  .cover-brand .brand-name{font:700 13px/0.95 Montserrat,sans-serif;color:#fff}
  .cover-kicker{position:absolute;top:76px;width:100%;text-align:center;color:#fff;font:600 9.5px Montserrat,sans-serif;letter-spacing:.3px}
  .cover-title{position:absolute;top:89px;width:100%;text-align:center;color:#fff;font:800 23.5px Montserrat,sans-serif;letter-spacing:.6px}
  .socials{position:absolute;top:126px;left:0;width:100%;display:flex;justify-content:center;gap:3px}
  .socials span{width:8px;height:8px;border-radius:50%;background:#fff}

  /* content slide chrome */
  .brand{position:absolute;left:15px;top:5px;display:flex;align-items:center;gap:3px}
  .brand-mark{width:11px;height:11px;background:var(--accent)}
  .brand-name{font:700 8px/0.95 Montserrat,sans-serif;color:var(--ink)}
  .slide-title{position:absolute;right:37px;top:9px;font:800 11.5px Montserrat,sans-serif;color:var(--ink);letter-spacing:.3px}
  .title-flag{position:absolute;left:281px;top:4px;width:13px;height:25px;background:var(--accent);clip-path:polygon(100% 0,100% 100%,0 50%)}
  .footer{position:absolute;left:0;bottom:0;width:100%;height:12px;background:var(--accent);color:#fff;font:500 3px Roboto,sans-serif;display:flex;align-items:center;justify-content:center}

  .photo{position:absolute;width:130px;height:108.5px}
  .photo-warm{background:linear-gradient(135deg,#5d6a72 0%,#8b7a68 45%,#3b3a3c 100%)}
  .photo-room{background:linear-gradient(120deg,#8b7b66 0%,#c9bfae 45%,#4a4640 100%)}
  .photo-table{background:linear-gradient(140deg,#b8a48a 0%,#6b5d52 50%,#d8d2c8 100%)}
  .photo-block{position:absolute;width:130px;height:108.5px;background:var(--accent)}
  .photo-outline{position:absolute;width:129px;height:110px;border:1.5px solid var(--accent)}

  .copy{position:absolute;width:128.5px;font:400 5.6px/9.4px Roboto,sans-serif;color:var(--copy);text-align:justify}

  /* why us */
  .why-diagram{position:absolute;left:0;top:0;width:311px;height:163px}
  .why-item{position:absolute;width:115px}
  .why-item h3{font:700 5px Montserrat,sans-serif;color:var(--ink)}
  .why-item h3::after{content:"";display:block;width:7px;height:.8px;background:var(--accent);margin:1.5px 0 1.5px}
  .why-item p{font:400 3px/5.4px Roboto,sans-serif;color:var(--copy)}

  /* testimonials */
  .quote-box{position:absolute;left:25px;top:49px;width:268.5px;height:94px;background:var(--tint);text-align:center;padding:0 26px}
  .quote-mark{display:block;font:800 26px/1 Montserrat,sans-serif;color:var(--accent);margin-top:7px;height:20px}
  .quote-text{font:400 5.6px/9.4px Roboto,sans-serif;color:var(--copy)}
  .quote-name{margin-top:2px;font:700 5.6px Roboto,sans-serif;color:var(--quote-name)}
</style>
</head>
<body>

<!-- ===== Business theme ===== -->
<section class="slide cover theme-business col-left row-1">
  <div class="cover-photo" role="img" aria-label="Tinted photo of a group in a coaching session"></div>
  <div class="cover-brand"><span class="brand-mark"></span><span class="brand-name">Bridge<br>of Valor</span></div>
  <p class="cover-kicker">WELCOME TO</p>
  <h1 class="cover-title">BRIDGE OF VALOR</h1>
  <div class="socials"><span></span><span></span><span></span></div>
</section>

<section class="slide theme-business col-left row-2">
  <div class="brand"><span class="brand-mark"></span><span class="brand-name">Bridge<br>of Valor</span></div>
  <h2 class="slide-title">PERSONAL</h2><span class="title-flag"></span>
  <div class="photo-block" style="left:19.5px;top:40px"></div>
  <div class="photo photo-warm" style="left:16px;top:37.5px" role="img" aria-label="Photo of a coach talking with two participants"></div>
  <p class="copy" style="left:165.5px;top:49px">Do you keep running into the same things and are you done with them? Do you want to grow? Rise above yourself? Give yourself that positive spin on your life and let your energy flow again. Follow your heart, use your mind and discover what is really inside you during our Valor training, coaching or workshops. Together we lay the foundation for your happiness.</p>
  <div class="footer">© 2024 Bridge of Valor.. All Rights Reserved</div>
</section>

<section class="slide theme-business col-left row-3">
  <div class="brand"><span class="brand-mark"></span><span class="brand-name">Bridge<br>of Valor</span></div>
  <h2 class="slide-title">WHY US ?</h2><span class="title-flag"></span>
  <svg class="why-diagram" viewBox="0 0 311 163">
    <g stroke="var(--accent)" stroke-width="0.8">
      <line x1="110" y1="49.5" x2="142" y2="49.5"/><line x1="122" y1="78" x2="170" y2="78"/>
      <line x1="122" y1="107" x2="142" y2="107"/><line x1="110" y1="135.5" x2="170" y2="135.5"/>
    </g>
    <circle cx="70" cy="95.5" r="53" fill="var(--accent)"/>
    <circle cx="71" cy="97" r="45" fill="#cfd2d3"/>
    <circle cx="70" cy="95.5" r="44" fill="#fff"/>
    <rect x="34" y="90" width="9" height="9" fill="var(--accent)"/>
    <text x="46" y="93.5" font-family="Montserrat,sans-serif" font-weight="700" font-size="9.5" fill="var(--ink)">Bridge</text>
    <text x="46" y="103" font-family="Montserrat,sans-serif" font-weight="700" font-size="9.5" fill="var(--ink)">of Valor</text>
    <g fill="var(--accent)"><circle cx="155.5" cy="49.5" r="14"/><circle cx="183.5" cy="78" r="14"/><circle cx="155.5" cy="107" r="14"/><circle cx="183.5" cy="135.5" r="14"/></g>
    <g fill="#fff">
      <path d="M155.5 55 l-5-5 a3 3 0 0 1 5-3.5 a3 3 0 0 1 5 3.5z"/>
      <rect x="177" y="80" width="2.5" height="5"/><rect x="181" y="77" width="2.5" height="8"/><rect x="185" y="74" width="2.5" height="11"/>
      <circle cx="183.5" cy="132" r="3"/><path d="M178 142 a5.5 5.5 0 0 1 11 0z"/>
    </g>
    <g fill="none" stroke="#fff" stroke-width="1">
      <path d="M176 76 l5-4 3 2 6-5"/>
      <rect x="150.5" y="100.5" width="10" height="13"/>
      <path d="M152.5 104 l1 1 2-2 M152.5 108 l1 1 2-2 M157 104.5 h2 M157 108.5 h2"/>
    </g>
  </svg>
  <div class="why-item" style="left:176.5px;top:40px"><h3>To the core</h3><p>Your ‘home’: the core where you and/or your team perform optimally. Where everyone feels good. That's what you look for. And that feels like coming home.</p></div>
  <div class="why-item" style="left:205px;top:69px"><h3>Grow</h3><p>We set people and organizations in motion. Let them grow. No ‘go with the flow’, but on your own strength and from your own conscious choices.</p></div>
  <div class="why-item" style="left:176.5px;top:98px"><h3>Specific</h3><p>Together we go into depth. We find out what is really going on and tackle the essence. This way you actually give your life a positive spin.</p></div>
  <div class="why-item" style="left:205px;top:126.5px"><h3>Concerned</h3><p>To help you further; that's why we get up in the morning. Driven, astute and committed, we let you discover how you can make an impact.</p></div>
  <div class="footer">© 2024 Bridge of Valor.. All Rights Reserved</div>
</section>

<section class="slide theme-business col-left row-4">
  <div class="brand"><span class="brand-mark"></span><span class="brand-name">Bridge<br>of Valor</span></div>
  <h2 class="slide-title">COMMERCIAL</h2><span class="title-flag"></span>
  <p class="copy" style="left:14.5px;top:48px">Are you struggling with your work? Or is it time for a breath of fresh air for your team? In short: do you want to bring passion back to the workplace? Let's get started. Mapping the knowledge, qualities and personalities of you and/or your team. Making the invisible visible. To then create space for understanding, better collaboration, innovation and creativity. And for fun!</p>
  <div class="photo-block" style="left:164px;top:40px"></div>
  <div class="photo photo-room" style="left:161.5px;top:37.5px" role="img" aria-label="Photo of a team seated in a circle during a workshop"></div>
  <div class="footer">© 2024 Bridge of Valor.. All Rights Reserved</div>
</section>

<section class="slide theme-business col-left row-5">
  <div class="brand"><span class="brand-mark"></span><span class="brand-name">Bridge<br>of Valor</span></div>
  <h2 class="slide-title">EDUCATIONS</h2><span class="title-flag"></span>
  <div class="photo photo-table" style="left:16px;top:42px" role="img" aria-label="Photo of participants working together over a table"></div>
  <div class="photo-outline" style="left:21px;top:37px"></div>
  <p class="copy" style="left:165.5px;top:70px">Do you also want to become a coach, guide teams or work on organizational change? Give your professional development a boost with a recognized post-higher professional education or with a practical and compact course.</p>
  <div class="footer">© 2024 Bridge of Valor.. All Rights Reserved</div>
</section>

<section class="slide theme-business col-left row-6">
  <div class="brand"><span class="brand-mark"></span><span class="brand-name">Bridge<br>of Valor</span></div>
  <h2 class="slide-title">OUR TESTIMONIALS</h2><span class="title-flag"></span>
  <div class="quote-box">
    <span class="quote-mark">“</span>
    <p class="quote-text">The BOV team creates a very pleasant and safe atmosphere in a short time. The trainers are very pleasant and empathetic, it is amazing how they get deeper and deeper into the core through targeted questions. The training has given me many new insights - both at work and privately. In addition, the training has given me the final push to make a personal wish become reality!</p>
    <p class="quote-name">Marit Management Supporter</p>
  </div>
  <div class="footer">© 2024 Bridge of Valor.. All Rights Reserved</div>
</section>

<!-- ===== Education theme ===== -->
<section class="slide cover theme-education col-right row-1">
  <div class="cover-photo" role="img" aria-label="Tinted photo of a group in a coaching session"></div>
  <div class="cover-brand"><span class="brand-mark"></span><span class="brand-name">Bridge<br>of Valor</span></div>
  <p class="cover-kicker">WELCOME TO</p>
  <h1 class="cover-title">BRIDGE OF VALOR</h1>
  <div class="socials"><span></span><span></span><span></span></div>
</section>

<section class="slide theme-education col-right row-2">
  <div class="brand"><span class="brand-mark"></span><span class="brand-name">Bridge<br>of Valor</span></div>
  <h2 class="slide-title">PERSONAL</h2><span class="title-flag"></span>
  <div class="photo-block" style="left:19.5px;top:40px"></div>
  <div class="photo photo-warm" style="left:16px;top:37.5px" role="img" aria-label="Photo of a coach talking with two participants"></div>
  <p class="copy" style="left:165.5px;top:49px">Do you keep running into the same things and are you done with them? Do you want to grow? Rise above yourself? Give yourself that positive spin on your life and let your energy flow again. Follow your heart, use your mind and discover what is really inside you during our Valor training, coaching or workshops. Together we lay the foundation for your happiness.</p>
  <div class="footer">© 2024 Bridge of Valor.. All Rights Reserved</div>
</section>

<section class="slide theme-education col-right row-3">
  <div class="brand"><span class="brand-mark"></span><span class="brand-name">Bridge<br>of Valor</span></div>
  <h2 class="slide-title">WHY US ?</h2><span class="title-flag"></span>
  <svg class="why-diagram" viewBox="0 0 311 163">
    <g stroke="var(--accent)" stroke-width="0.8">
      <line x1="110" y1="49.5" x2="142" y2="49.5"/><line x1="122" y1="78" x2="170" y2="78"/>
      <line x1="122" y1="107" x2="142" y2="107"/><line x1="110" y1="135.5" x2="170" y2="135.5"/>
    </g>
    <circle cx="70" cy="95.5" r="53" fill="var(--accent)"/>
    <circle cx="71" cy="97" r="45" fill="#cfd2d3"/>
    <circle cx="70" cy="95.5" r="44" fill="#fff"/>
    <rect x="34" y="90" width="9" height="9" fill="var(--accent)"/>
    <text x="46" y="93.5" font-family="Montserrat,sans-serif" font-weight="700" font-size="9.5" fill="var(--ink)">Bridge</text>
    <text x="46" y="103" font-family="Montserrat,sans-serif" font-weight="700" font-size="9.5" fill="var(--ink)">of Valor</text>
    <g fill="var(--accent)"><circle cx="155.5" cy="49.5" r="14"/><circle cx="183.5" cy="78" r="14"/><circle cx="155.5" cy="107" r="14"/><circle cx="183.5" cy="135.5" r="14"/></g>
    <g fill="#fff">
      <path d="M155.5 55 l-5-5 a3 3 0 0 1 5-3.5 a3 3 0 0 1 5 3.5z"/>
      <rect x="177" y="80" width="2.5" height="5"/><rect x="181" y="77" width="2.5" height="8"/><rect x="185" y="74" width="2.5" height="11"/>
      <circle cx="183.5" cy="132" r="3"/><path d="M178 142 a5.5 5.5 0 0 1 11 0z"/>
    </g>
    <g fill="none" stroke="#fff" stroke-width="1">
      <path d="M176 76 l5-4 3 2 6-5"/>
      <rect x="150.5" y="100.5" width="10" height="13"/>
      <path d="M152.5 104 l1 1 2-2 M152.5 108 l1 1 2-2 M157 104.5 h2 M157 108.5 h2"/>
    </g>
  </svg>
  <div class="why-item" style="left:176.5px;top:40px"><h3>To the core</h3><p>Your ‘home’: the core where you and/or your team perform optimally. Where everyone feels good. That's what you look for. And that feels like coming home.</p></div>
  <div class="why-item" style="left:205px;top:69px"><h3>Grow</h3><p>We set people and organizations in motion. Let them grow. No ‘go with the flow’, but on your own strength and from your own conscious choices.</p></div>
  <div class="why-item" style="left:176.5px;top:98px"><h3>Specific</h3><p>Together we go into depth. We find out what is really going on and tackle the essence. This way you actually give your life a positive spin.</p></div>
  <div class="why-item" style="left:205px;top:126.5px"><h3>Concerned</h3><p>To help you further; that's why we get up in the morning. Driven, astute and committed, we let you discover how you can make an impact.</p></div>
  <div class="footer">© 2024 Bridge of Valor.. All Rights Reserved</div>
</section>

<section class="slide theme-education col-right row-4">
  <div class="brand"><span class="brand-mark"></span><span class="brand-name">Bridge<br>of Valor</span></div>
  <h2 class="slide-title">COMMERCIAL</h2><span class="title-flag"></span>
  <p class="copy" style="left:14.5px;top:48px">Are you struggling with your work? Or is it time for a breath of fresh air for your team? In short: do you want to bring passion back to the workplace? Let's get started. Mapping the knowledge, qualities and personalities of you and/or your team. Making the invisible visible. To then create space for understanding, better collaboration, innovation and creativity. And for fun!</p>
  <div class="photo-block" style="left:164px;top:40px"></div>
  <div class="photo photo-room" style="left:161.5px;top:37.5px" role="img" aria-label="Photo of a team seated in a circle during a workshop"></div>
  <div class="footer">© 2024 Bridge of Valor.. All Rights Reserved</div>
</section>

<section class="slide theme-education col-right row-5">
  <div class="brand"><span class="brand-mark"></span><span class="brand-name">Bridge<br>of Valor</span></div>
  <h2 class="slide-title">EDUCATIONS</h2><span class="title-flag"></span>
  <div class="photo photo-table" style="left:16px;top:42px" role="img" aria-label="Photo of participants working together over a table"></div>
  <div class="photo-outline" style="left:21px;top:37px"></div>
  <p class="copy" style="left:165.5px;top:70px">Do you also want to become a coach, guide teams or work on organizational change? Give your professional development a boost with a recognized post-higher professional education or with a practical and compact course.</p>
  <div class="footer">© 2024 Bridge of Valor.. All Rights Reserved</div>
</section>

<section class="slide theme-education col-right row-6">
  <div class="brand"><span class="brand-mark"></span><span class="brand-name">Bridge<br>of Valor</span></div>
  <h2 class="slide-title">OUR TESTIMONIALS</h2><span class="title-flag"></span>
  <div class="quote-box">
    <span class="quote-mark">“</span>
    <p class="quote-text">The BOV team creates a very pleasant and safe atmosphere in a short time. The trainers are very pleasant and empathetic, it is amazing how they get deeper and deeper into the core through targeted questions. The training has given me many new insights - both at work and privately. In addition, the training has given me the final push to make a personal wish become reality!</p>
    <p class="quote-name">Marit Management Supporter</p>
  </div>
  <div class="footer">© 2024 Bridge of Valor.. All Rights Reserved</div>
</section>

</body>
</html>
```